One of Australia's fastest growing Financial Company looking for an updated business card design!

Meridale Holdings Australia is looking for an updated design for our business cards. We would like to keep up our professional appearances and have get new exciting design that fits our company.

The Meridale aim is to facilitate and assist clients in every financial requirement that may arise in financial areas.

We would to see the design to use colour blue and we like the clouds in the background. We have attached two designs we have use before but we need something with more professional and easy to read design.

We would like the website in the back of the card; the employees name more central and stands out; only a postal address; a list of all our locations along the bottom (Sydney, Melbourne, Brisbane, Singapore)

Looking forward to seeing the designs come in!

Target Market(s)

Other Industry Professionals
Middle Class Families

Industry/Entity Type

Finance

Contact Information for Business Card

Name; Company Role; Office Number; Mobile Number; Email Address; Website; Postal Address; Locations

Font styles to use
Serif
Sans Serif

Colors
0492cd
33a6d7
85cae6
85acd3
3176b5
0455a3
cee9f5
d5e2ee

Requirements
Must have
• Name; Company Role; Office Number; Mobile Number; Email Address; Website; Postal Address; Locations
Nice to have
• The colour blue, clouds on the background

```html
<!DOCTYPE html>
<html lang="en">
<head>
<meta charset="utf-8">
<title>Meridale Holdings Australia – Business Card</title>
<link rel="stylesheet" href="https://fonts.googleapis.com/css2?family=Open+Sans:ital,wght@0,400;0,700;1,400;1,600&display=swap">
<style>
  :root {
    --stage: #505d6b;
    --label: #ffffff;
    --sky-top: #e9f5f4;
    --sky-mid: #8fc9c4;
    --sky-low: #5ea5a4;
    --navy: #0716b0;
    --accent-red: #e8283f;
    --brand-blue: #33a6d7;
    --ink: #111111;
    --paper: #ffffff;
    --paper-tint: #d8f1f3;
  }
  * { margin: 0; padding: 0; box-sizing: border-box; }
  html, body { width: 1000px; height: 1200px; overflow: hidden; }
  body {
    background: var(--stage);
    font-family: "Open Sans", Arial, sans-serif;
    position: relative;
  }
  .side-label {
    position: absolute;
    color: var(--label);
    font-size: 40px;
    font-weight: 400;
    letter-spacing: 1px;
  }
  .side-label--front { left: 380px; top: 150px; }
  .side-label--back { left: 803px; top: 888px; }

  .card {
    position: absolute;
    width: 614px;
    height: 350px;
    overflow: hidden;
    box-shadow: 0 20px 40px rgba(0,0,0,0.35);
  }
  .card--front { left: 250px; top: 215px; }
  .card--back { left: 180px; top: 590px; background: var(--paper); }

  .sky-backdrop {
    position: absolute; inset: 0;
    background:
      radial-gradient(ellipse at 70% 85%, rgba(255,255,255,0.6), transparent 55%),
      linear-gradient(160deg, var(--sky-top) 0%, var(--sky-mid) 45%, var(--sky-low) 100%);
  }
  .front-brand {
    position: absolute;
    left: 0; right: 0; top: 135px;
    display: flex; align-items: center; justify-content: center; gap: 16px;
  }
  .brand-dot {
    width: 48px; height: 48px; border-radius: 50%;
    background: var(--accent-red);
  }
  .front-brand .brand-name {
    color: var(--paper);
    font-size: 66px;
    font-weight: 400;
    line-height: 1;
  }

  .back-shape { position: absolute; inset: 0; }
  .back-brand {
    position: absolute;
    right: 30px; top: 20px;
    display: flex; align-items: center; gap: 10px;
  }
  .back-brand .brand-dot { width: 30px; height: 30px; }
  .back-brand .brand-name {
    color: var(--brand-blue);
    font-size: 42px;
    font-weight: 400;
    line-height: 1;
  }
  .website {
    position: absolute;
    right: 58px; top: 72px;
    color: var(--paper);
    font-size: 13px;
    font-style: italic;
    font-weight: 600;
  }
  .holder { position: absolute; left: 18px; top: 98px; }
  .holder-name { font-size: 26px; font-weight: 700; color: var(--ink); line-height: 1.2; }
  .holder-role { font-size: 17px; font-style: italic; color: var(--ink); line-height: 1.2; }
  .contact-list {
    position: absolute; left: 18px; top: 183px;
    list-style: none;
    font-size: 15.5px; color: var(--ink); line-height: 20px;
  }
  .contact-list .locations { margin-top: 4px; }
</style>
</head>
<body>
  <div class="side-label side-label--front">FRONT</div>
  <section class="card card--front">
    <div class="sky-backdrop" role="img" aria-label="Soft teal sky with clouds"></div>
    <div class="front-brand">
      <span class="brand-dot"></span>
      <span class="brand-name">Meridale</span>
    </div>
  </section>

  <section class="card card--back">
    <svg class="back-shape" width="614" height="350" viewBox="0 0 614 350">
      <defs>
        <linearGradient id="paperWash" x1="0" y1="0" x2="1" y2="1">
          <stop offset="0" stop-color="#cfeef1"/>
          <stop offset="0.6" stop-color="#f2fbfc"/>
          <stop offset="1" stop-color="#ffffff"/>
        </linearGradient>
      </defs>
      <rect width="614" height="350" fill="url(#paperWash)" role="img" aria-label="Faint light aqua faceted background"/>
      <path d="M0,0 L614,0 L614,350 L600,350 Q470,60 0,0 Z" fill="var(--navy)"/>
      <path d="M0,0 Q470,60 600,350" fill="none" stroke="var(--accent-red)" stroke-width="3"/>
    </svg>
    <div class="back-brand">
      <span class="brand-dot"></span>
      <span class="brand-name">Meridale</span>
    </div>
    <div class="website">www.meridaleholdings.com.au</div>
    <div class="holder">
      <div class="holder-name">Daniel Hart</div>
      <div class="holder-role">Manager</div>
    </div>
    <ul class="contact-list">
      <li>48 Harbour Road Coffs Harbour NSW 2450</li>
      <li>(02) 6651 7280</li>
      <li>1800 – MERI – DALE</li>
      <li>1800&nbsp; 6374&nbsp; 3253</li>
      <li>info@meridaleholdings.com.au</li>
      <li class="locations">(Sydney, Melbourne, Brisbane, Singapore)</li>
    </ul>
  </section>
  <div class="side-label side-label--back">BACK</div>
</body>
</html>
```